Bref créative
Company Sales Brochure
3 Fold Sales Brochure
Unified Marketing Platform
Looking for a 3 fold marketing brochure based on information obtained from our web site www.quentrivo.com
Information Technology
Small Business
Use color scheme and design similar to our website www.quentrivo.com and our business cards http://aws.quentrivo.com/common/business-card-dale.png
Our Logo file (illustrator)
Our Logo file (png)

```html
<!DOCTYPE html>
<html lang="en">
<head>
<meta charset="utf-8">
<title>QUENTRIVO – Unified Marketing Platform Brochure</title>
<link href="https://fonts.googleapis.com/css2?family=Roboto:wght@400;500;700&family=Roboto+Condensed:wght@400;700&display=swap" rel="stylesheet">
<style>
  :root{
    --bg:#e9ecf0;
    --navy:#0b2c5a;
    --blue:#0a4f9c;
    --mid:#1f7fd0;
    --sky:#59a8e6;
    --pale:#d7ebfa;
    --paper:#ffffff;
    --ink:#3a4654;
    --muted:#6b7786;
  }
  *{margin:0;padding:0;box-sizing:border-box}
  html,body{width:1200px;height:989px;overflow:hidden;background:var(--bg)}
  body{font-family:"Roboto",Arial,sans-serif;color:var(--ink);position:relative}
  .spread{position:absolute;left:20px;width:1160px;height:462px;display:flex;box-shadow:0 2px 10px rgba(0,0,0,.18);background:var(--paper)}
  .spread--outside{top:20px}
  .spread--inside{top:507px}
  .panel{position:relative;width:386.67px;height:100%;overflow:hidden}
  .panel + .panel{border-left:1px solid #dfe6ee}
  .photo{background:linear-gradient(135deg,#9fc6e6,#5a8fbf 60%,#2e5f92)}
  .wave{position:absolute;left:0;bottom:0;width:100%;height:70px}
  .web{position:absolute;bottom:10px;right:18px;font:700 15px "Roboto",sans-serif;color:#fff;letter-spacing:.3px}
  p.body{font-size:7.6px;line-height:1.45;color:var(--ink)}

  /* About */
  .about__bar{background:linear-gradient(90deg,var(--blue),var(--mid));color:#fff;padding:9px 16px;font:700 17px "Roboto Condensed",sans-serif}
  .about__inner{padding:10px 16px}
  .about h3{font:700 10px "Roboto",sans-serif;color:var(--blue);margin:8px 0 3px}
  .about__photo{height:92px;margin:8px 0}

  /* Testimonial */
  .testimonial{background:linear-gradient(180deg,#eaf4fc,#c7e0f5)}
  .testimonial__title{background:var(--blue);color:#fff;padding:9px 16px;font:700 17px "Roboto Condensed",sans-serif}
  .testimonial__quote{padding:12px 18px;font-size:8.4px;line-height:1.5;font-style:italic;color:var(--navy)}
  .testimonial__who{display:block;text-align:right;font-style:normal;font-weight:700;margin-top:4px}
  .testimonial__photo{position:absolute;left:30px;top:120px;width:150px;height:170px;border-radius:6px}
  .contact{position:absolute;left:30px;top:310px;font-size:8.5px;line-height:1.6;color:var(--navy)}
  .contact svg{width:9px;height:9px;vertical-align:-1px;margin-right:4px;fill:var(--blue)}

  /* Cover */
  .cover__top{height:215px;background:#fff;padding:16px 20px;position:relative}
  .logo{display:flex;align-items:center;gap:8px;border:2px solid var(--blue);padding:6px 12px;width:max-content;margin:0 auto}
  .logo__mark{width:14px;height:14px;background:var(--mid)}
  .logo__name{font:700 24px "Roboto",sans-serif;color:var(--blue);letter-spacing:1px}
  .cover__tag{text-align:center;font:700 12px "Roboto",sans-serif;color:var(--blue);margin-top:10px}
  .cover__list{text-align:center;font-size:7.6px;color:var(--muted);margin-top:3px;line-height:1.4}
  .cover__photo{position:absolute;left:20px;right:20px;bottom:8px;height:92px}
  .cover__band{position:absolute;top:215px;left:0;right:0;bottom:0;background:linear-gradient(180deg,#f4f9fe,#d7ebfa)}
  .cover__title{position:absolute;left:22px;top:26px;font:700 25px/1.15 "Roboto Condensed",sans-serif;color:var(--mid)}
  .cover__title span{display:block;color:var(--navy);font-size:22px}

  /* Process */
  .process__head{height:140px;position:relative;background:linear-gradient(160deg,#0b2c5a,#1f7fd0)}
  .process__title{position:absolute;left:16px;top:14px;color:#fff;font:700 26px "Roboto Condensed",sans-serif}
  .process__group{position:absolute;left:16px;right:16px;bottom:0;height:78px}
  .phase{margin:9px 16px 0}
  .phase__label{font-size:9.5px;color:var(--blue);font-weight:700}
  .phase__label b{display:inline-block;background:var(--mid);color:#fff;font-size:7px;padding:1px 4px;margin-right:5px;border-radius:2px}
  .intro{margin:10px 16px 0}
  .steps__photo{height:96px}
  .steps .phase{margin-top:11px}

  /* Services */
  .services{background:linear-gradient(180deg,#f4f9fe,#ffffff 55%)}
  .services__title{font:700 18px "Roboto Condensed",sans-serif;color:var(--blue);padding:16px 20px 6px}
  .services ul{list-style:none;padding:0 20px}
  .services li{font-size:9px;color:var(--navy);line-height:1.75;display:flex;align-items:center;gap:6px}
  .services li::before{content:"";width:6px;height:6px;background:var(--mid);border-radius:50%}
  .services__visual{position:absolute;left:40px;right:40px;top:205px;height:170px;border-radius:6px;background:linear-gradient(180deg,#a9d2f2,#3f86c9 70%,#1c5a9e)}
</style>
</head>
<body>

<section class="spread spread--outside" aria-label="Brochure outside">
  <article class="panel about">
    <div class="about__bar">About QUENTRIVO</div>
    <div class="about__inner">
      <h3>Quality Services at Affordable Prices</h3>
      <p class="body">QUENTRIVO is a trusted provider of software that helps small businesses market smarter, sell faster and grow steadily with one simple platform.</p>
      <div class="about__photo photo" role="img" aria-label="Photo of the company office building"></div>
      <h3>Communication</h3>
      <p class="body">We keep every client informed at each step, with clear reports and open lines so nothing about your campaign is ever a mystery.</p>
      <h3>We Listen Carefully</h3>
      <p class="body">Your goals shape our plan. We take time to learn your market, your customers and your budget before we suggest a single tool.</p>
    </div>
  </article>

  <article class="panel testimonial">
    <div class="testimonial__title">Testimonial</div>
    <p class="testimonial__quote">“Since switching to this platform our leads have doubled and our team spends less time on busy work and more time closing sales.”
      <span class="testimonial__who">— Marla Dennison, Owner</span></p>
    <div class="testimonial__photo photo" role="img" aria-label="Photo of a smiling support agent with headset"></div>
    <div class="contact">
      <div><svg viewBox="0 0 10 10"><path d="M5 0a3.5 3.5 0 0 0-3.5 3.5C1.5 6 5 10 5 10s3.5-4 3.5-6.5A3.5 3.5 0 0 0 5 0zm0 5a1.5 1.5 0 1 1 0-3 1.5 1.5 0 0 1 0 3z"/></svg>2200 Harbor Crest Ave, Suite 410</div>
      <div><svg viewBox="0 0 10 10"><path d="M2 0l2 2-1 1.5c.7 1.5 2 2.8 3.5 3.5L8 6l2 2-1.5 2C4 10 0 6 0 1.5z"/></svg>(555) 014-2288</div>
      <div>hello@quentrivo.com</div>
    </div>
    <svg class="wave" viewBox="0 0 387 70" preserveAspectRatio="none"><path d="M0 30 Q120 0 240 25 T387 15 V70 H0z" fill="#1f7fd0"/><path d="M0 45 Q140 20 260 42 T387 32 V70 H0z" fill="#0a4f9c"/></svg>
  </article>

  <article class="panel cover">
    <div class="cover__top">
      <div class="logo"><span class="logo__mark"></span><span class="logo__name">QUENTRIVO</span></div>
      <div class="cover__tag">Unified Marketing Platform</div>
      <div class="cover__list">Web Design · Email Campaigns · Lead Tracking<br>CRM · Social Media · Analytics · Reports</div>
      <div class="cover__photo photo" role="img" aria-label="Photo of a business team working together"></div>
    </div>
    <div class="cover__band">
      <div class="cover__title">Unified Marketing Platform<span>All-in One Sales and<br>Marketing Tool</span></div>
      <svg class="wave" viewBox="0 0 387 70" preserveAspectRatio="none"><path d="M0 25 Q130 0 250 28 T387 12 V70 H0z" fill="#59a8e6"/><path d="M0 40 Q150 18 270 40 T387 28 V70 H0z" fill="#0a4f9c"/></svg>
      <div class="web">www.quentrivo.com</div>
    </div>
  </article>
</section>

<section class="spread spread--inside" aria-label="Brochure inside">
  <article class="panel process">
    <div class="process__head">
      <div class="process__title">OUR PROCESS</div>
      <div class="process__group photo" role="img" aria-label="Photo of a group of business professionals"></div>
    </div>
    <p class="body intro">At QUENTRIVO we follow a proven six phase process that turns your ideas into measurable results, keeping you involved from first call to final training.</p>
    <div class="phase"><div class="phase__label"><b>Phase 1</b>Consultation</div>
      <p class="body">We meet with you to review your goals, current tools and challenges, then outline a plan that fits your business and budget.</p></div>
    <div class="phase"><div class="phase__label"><b>Phase 2</b>Analysis</div>
      <p class="body">Our team studies your market, competitors and website traffic to find the quickest wins and the best long term opportunities.</p></div>
  </article>

  <article class="panel steps">
    <div class="steps__photo photo" role="img" aria-label="Photo of colleagues meeting in an office"></div>
    <div class="phase"><div class="phase__label"><b>Phase 3</b>Proposal &amp; Review</div>
      <p class="body">You receive a clear proposal with scope, timeline and pricing, and we refine it together until every detail is right.</p></div>
    <div class="phase"><div class="phase__label"><b>Phase 4</b>Development</div>
      <p class="body">We configure the platform, build your pages and connect your data so your campaigns are ready to launch.</p></div>
    <div class="phase"><div class="phase__label"><b>Phase 5</b>Testing</div>
      <p class="body">Every form, email and report is tested carefully across devices so your launch goes smoothly with no surprises.</p></div>
    <div class="phase"><div class="phase__label"><b>Phase 6</b>Training</div>
      <p class="body">We train your staff on daily use of the system and stay available for support long after the project is done.</p></div>
    <svg class="wave" viewBox="0 0 387 70" preserveAspectRatio="none"><path d="M0 35 Q130 10 250 35 T387 22 V70 H0z" fill="#1f7fd0"/><path d="M0 48 Q150 28 270 48 T387 38 V70 H0z" fill="#0a4f9c"/></svg>
    <div class="web">www.quentrivo.com</div>
  </article>

  <article class="panel services">
    <div class="services__title">Our Services</div>
    <ul>
      <li>Search Engine Optimization</li>
      <li>Call Tracking</li>
      <li>Lead Management (CRM)</li>
      <li>Advanced Management</li>
      <li>Reporting &amp; Analytics</li>
      <li>Email Marketing</li>
      <li>Social Media Marketing</li>
      <li>Web Development</li>
    </ul>
    <div class="services__visual" role="img" aria-label="Illustration of a glossy blue sales funnel"></div>
    <svg class="wave" viewBox="0 0 387 70" preserveAspectRatio="none"><path d="M0 30 Q120 5 240 30 T387 18 V70 H0z" fill="#59a8e6"/><path d="M0 46 Q140 24 260 46 T387 34 V70 H0z" fill="#0a4f9c"/></svg>
  </article>
</section>

</body>
</html>
```